A social health network MOBILE APP needs an awesome home page

We need a home page design that is attractive, and simple to navigate for our mobile app. This app helps people maintain their personal health records, find and connect with care providers to ask question, get care online or face to face through appointment. It also has a few other features to encourage engagement such as Forum, Reward, Service Discount Coupon.
We would like to see the design that uses the color green (our company color) as the main color, and includes an area for announcement plus another area for advertising. We include sketches of our need for your review.
The final design should look modern, friendly, and lively.
Updates
If possible, please break away from our attached sketch format and let your creativity leads the way? We would like to see the bottom buttons layout in differently from the sketch.
Industry/Entity Type
Health
Colors
Designer to choose colors to be used in the design.
Requirements
Must have
- A clean and elegant look.

```html
<!DOCTYPE html>
<html lang="en">
<head>
<meta charset="utf-8">
<title>Health Network – Home</title>
<link rel="stylesheet" href="https://fonts.googleapis.com/css2?family=Dancing+Script:wght@600&family=Ubuntu:wght@400&family=Roboto:wght@400&display=swap">
<style>
  :root{
    --status-green:#86e03a;
    --header-green:#9cf047;
    --accent:#8ee44c;
    --label:#7ed83c;
    --screen-bg:#e4e6e6;
    --panel-bg:#eaeaea;
    --white:#ffffff;
    --ink:#111111;
  }
  *{box-sizing:border-box;margin:0;padding:0}
  html,body{width:1200px;height:939px;overflow:hidden;background:var(--white)}
  .canvas{position:relative;width:1200px;height:939px}
  .screen{position:absolute;top:20px;width:512px;height:909px;background:var(--screen-bg);overflow:hidden}
  .screen--home{left:53px}
  .screen--scrolled{left:627px}
  .status-bar{position:absolute;left:0;top:0;width:100%;height:33px;background:var(--status-green)}
  .app-header{position:absolute;left:0;top:33px;width:100%;height:110px;background:var(--header-green)}
  .menu-icon{position:absolute;left:24px;top:30px}
  .search-icon{position:absolute;right:22px;top:28px}
  .app-title{position:absolute;left:0;right:0;top:16px;text-align:center;font-family:"Dancing Script",cursive;font-size:36px;color:var(--white)}
  .tabs{position:absolute;left:0;right:0;top:86px;display:flex;justify-content:space-around;padding:0 10px;
        font-family:"Roboto",Arial,sans-serif;font-size:15px;color:var(--white);letter-spacing:.2px}
  .tabs .is-active{border-bottom:2px solid rgba(0,0,0,.15);padding-bottom:1px}
  .ad-space{position:absolute;left:2px;right:2px}
  .ad-space--family{top:143px;height:194px;background:linear-gradient(100deg,#5b7386 0%,#6f8a5a 35%,#3f5a34 60%,#9db8c8 100%)}
  .ad-space--newborn{top:673px;height:236px;background:radial-gradient(ellipse at 45% 45%,#d9a0b0 0%,#6b4a52 32%,#2a2224 70%,#1a1a1c 100%)}
  .ad-note{position:absolute;right:8px;bottom:6px;font-family:Arial,sans-serif;font-size:12px;color:var(--ink)}
  .ad-space--newborn .ad-note{color:var(--white)}
  .quick-panel{position:absolute;left:0;top:337px;width:100%;height:190px;background:var(--panel-bg);box-shadow:0 6px 8px rgba(0,0,0,.12)}
  .tile{position:absolute;width:180px;margin-left:-90px;text-align:center}
  .tile__ring{margin:0 auto;border-radius:50%;border:4px solid var(--accent);background:var(--screen-bg);
              box-shadow:0 2px 5px rgba(0,0,0,.18);display:flex;align-items:center;justify-content:center}
  .tile--lg .tile__ring{width:93px;height:93px}
  .tile--sm .tile__ring{width:80px;height:80px;border-width:3px}
  .tile__label{display:block;margin-top:14px;font-family:"Ubuntu",sans-serif;font-size:20px;color:var(--label)}
  .tile--sm .tile__label{margin-top:16px}
  svg.glyph{fill:none;stroke:var(--accent);stroke-width:3;stroke-linecap:round;stroke-linejoin:round}
</style>
</head>
<body>
<div class="canvas">

  <svg width="0" height="0" style="position:absolute" aria-hidden="true">
    <symbol id="g-records" viewBox="0 0 40 40"><rect x="9" y="6" width="22" height="29" rx="2"/><rect x="15" y="3" width="10" height="6" rx="1"/><path d="M14 15h2M19 15h8M14 21h2M19 21h8M14 27h2M19 27h8"/></symbol>
    <symbol id="g-question" viewBox="0 0 40 40"><path d="M13 14a7 7 0 1 1 10 6c-2 1-3 3-3 5v2"/><circle cx="20" cy="32" r="1.2"/></symbol>
    <symbol id="g-pin" viewBox="0 0 40 40"><path d="M20 36s-10-11-10-19a10 10 0 0 1 20 0c0 8-10 19-10 19z"/><circle cx="20" cy="17" r="4"/></symbol>
    <symbol id="g-chat" viewBox="0 0 40 40"><ellipse cx="20" cy="17" rx="15" ry="10"/><path d="M12 25l-3 7 9-5"/></symbol>
    <symbol id="g-globe" viewBox="0 0 40 40"><circle cx="20" cy="20" r="13"/><path d="M7 20h26M20 7c5 4 5 22 0 26M20 7c-5 4-5 22 0 26"/><path d="M4 26c8 8 26 6 33-8"/></symbol>
    <symbol id="g-people" viewBox="0 0 40 40"><g fill="#8ee44c" stroke="none"><circle cx="24" cy="13" r="6"/><path d="M13 33c0-8 5-12 11-12s11 4 11 12z"/><circle cx="15" cy="15" r="5"/><path d="M5 33c0-7 4-11 10-11 3 0 5 1 6 2-3 2-5 5-5 9z"/></g></symbol>
    <symbol id="g-gift" viewBox="0 0 40 40"><rect x="7" y="16" width="26" height="18"/><rect x="5" y="11" width="30" height="6"/><path d="M20 11v23M20 11c-3-6-9-6-8-2 1 2 5 2 8 2zM20 11c3-6 9-6 8-2-1 2-5 2-8 2z"/></symbol>
    <symbol id="g-coin" viewBox="0 0 40 40"><circle cx="20" cy="20" r="15"/><circle cx="20" cy="20" r="11"/><path d="M24 15c-1-2-7-3-8 0s8 3 8 7-7 4-9 1M20 11v18"/></symbol>
    <symbol id="g-search" viewBox="0 0 40 40"><circle cx="17" cy="17" r="9"/><path d="M24 24l9 9" stroke-width="5"/></symbol>
    <symbol id="g-info" viewBox="0 0 40 40"><circle cx="22" cy="9" r="2"/><path d="M20 15c-3 6-7 15-5 18 2 2 6-2 8-4M13 31l4-2"/></symbol>
  </svg>

  <!-- Home screen -->
  <section class="screen screen--home">
    <div class="status-bar"></div>
    <header class="app-header">
      <svg class="menu-icon" width="34" height="26" viewBox="0 0 34 26"><path d="M2 3h30M2 13h30M2 23h30" stroke="#fff" stroke-width="3" stroke-linecap="round"/></svg>
      <div class="app-title">App Name or Logo</div>
      <svg class="search-icon" width="32" height="30" viewBox="0 0 32 30"><circle cx="12" cy="11" r="8" stroke="#fff" stroke-width="3" fill="none"/><path d="M18 17l10 9" stroke="#fff" stroke-width="5" stroke-linecap="round"/></svg>
      <nav class="tabs"><span class="is-active">HOME</span><span>FEED</span><span>NOTIFICATION</span><span>MESSAGE</span><span>SETTINGS</span></nav>
    </header>
    <div class="ad-space ad-space--family" role="img" aria-label="Advertising photo: a family sitting together in a forest">
      <span class="ad-note">*advertising space*</span>
    </div>
    <div class="quick-panel">
      <div class="tile tile--sm" style="left:84px;top:50px"><div class="tile__ring"><svg class="glyph" width="44" height="44"><use href="#g-records"/></svg></div><span class="tile__label">Records</span></div>
      <div class="tile tile--sm" style="left:244px;top:50px"><div class="tile__ring"><svg class="glyph" width="44" height="44"><use href="#g-question"/></svg></div><span class="tile__label">Questions</span></div>
      <div class="tile tile--sm" style="left:417px;top:50px"><div class="tile__ring"><svg class="glyph" width="44" height="44"><use href="#g-pin"/></svg></div><span class="tile__label">Find Service</span></div>
    </div>
    <div class="tile tile--lg" style="left:85px;top:580px"><div class="tile__ring"><svg class="glyph" width="54" height="54"><use href="#g-chat"/></svg></div><span class="tile__label">Forum</span></div>
    <div class="tile tile--lg" style="left:245px;top:580px"><div class="tile__ring"><svg class="glyph" width="54" height="54"><use href="#g-globe"/></svg></div><span class="tile__label">Connections</span></div>
    <div class="tile tile--lg" style="left:402px;top:580px"><div class="tile__ring"><svg class="glyph" width="54" height="54"><use href="#g-people"/></svg></div><span class="tile__label">Invite</span></div>
    <div class="tile tile--lg" style="left:85px;top:740px"><div class="tile__ring"><svg class="glyph" width="54" height="54"><use href="#g-gift"/></svg></div><span class="tile__label">Rewards</span></div>
    <div class="tile tile--lg" style="left:245px;top:740px"><div class="tile__ring"><svg class="glyph" width="54" height="54"><use href="#g-coin"/></svg></div><span class="tile__label">Coupons</span></div>
    <div class="tile tile--lg" style="left:402px;top:740px"><div class="tile__ring"><svg class="glyph" width="54" height="54"><use href="#g-search"/></svg></div><span class="tile__label">Scan Voucher</span></div>
    <div class="tile tile--lg" style="left:245px;top:895px"><div class="tile__ring"></div></div>
  </section>

  <!-- Scrolled home screen -->
  <section class="screen screen--scrolled">
    <div class="status-bar"></div>
    <header class="app-header">
      <svg class="menu-icon" width="34" height="26" viewBox="0 0 34 26"><path d="M2 3h30M2 13h30M2 23h30" stroke="#fff" stroke-width="3" stroke-linecap="round"/></svg>
      <div class="app-title">App Name or Logo</div>
      <svg class="search-icon" width="32" height="30" viewBox="0 0 32 30"><circle cx="12" cy="11" r="8" stroke="#fff" stroke-width="3" fill="none"/><path d="M18 17l10 9" stroke="#fff" stroke-width="5" stroke-linecap="round"/></svg>
      <nav class="tabs"><span class="is-active">HOME</span><span>FEED</span><span>NOTIFICATION</span><span>MESSAGE</span><span>SETTINGS</span></nav>
    </header>
    <div class="tile tile--lg" style="left:93px;top:160px"><div class="tile__ring"><svg class="glyph" width="54" height="54"><use href="#g-chat"/></svg></div><span class="tile__label">Forum</span></div>
    <div class="tile tile--lg" style="left:253px;top:160px"><div class="tile__ring"><svg class="glyph" width="54" height="54"><use href="#g-globe"/></svg></div><span class="tile__label">Connections</span></div>
    <div class="tile tile--lg" style="left:411px;top:160px"><div class="tile__ring"><svg class="glyph" width="54" height="54"><use href="#g-people"/></svg></div><span class="tile__label">Invite</span></div>
    <div class="tile tile--lg" style="left:93px;top:320px"><div class="tile__ring"><svg class="glyph" width="54" height="54"><use href="#g-gift"/></svg></div><span class="tile__label">Rewards</span></div>
    <div class="tile tile--lg" style="left:253px;top:320px"><div class="tile__ring"><svg class="glyph" width="54" height="54"><use href="#g-coin"/></svg></div><span class="tile__label">Coupons</span></div>
    <div class="tile tile--lg" style="left:411px;top:320px"><div class="tile__ring"><svg class="glyph" width="54" height="54"><use href="#g-search"/></svg></div><span class="tile__label">Scan Voucher</span></div>
    <div class="tile tile--lg" style="left:257px;top:493px"><div class="tile__ring"><svg class="glyph" width="54" height="54"><use href="#g-info"/></svg></div><span class="tile__label">Rewards</span></div>
    <div class="ad-space ad-space--newborn" role="img" aria-label="Advertising photo: parents' hands holding a newborn's feet">
      <span class="ad-note">*advertising space*</span>
    </div>
  </section>

</div>
</body>
</html>
```